Professional modern business card design

A business card for my nutrition business, wanting a professional look, with info clearly visible. Open to using logo colours too.

Would like key info on the front -
logo
my name and qualifications
email
phone number

and just an enlarged logo again / image on the back.

```html
<!DOCTYPE html>
<html lang="en">
<head>
<meta charset="utf-8">
<title>Halden Nutrition – Business Card</title>
<link rel="stylesheet" href="https://fonts.googleapis.com/css2?family=Lato:wght@400;700;900&display=swap">
<style>
  :root {
    --backdrop: #1d1d1d;
    --card-navy: #00293f;
    --accent-lime: #d5e021;
    --text-white: #ffffff;
  }
  * { margin: 0; padding: 0; box-sizing: border-box; }
  html, body {
    width: 1200px;
    height: 1200px;
    overflow: hidden;
    background: var(--backdrop);
    font-family: 'Lato', sans-serif;
  }
  .stage {
    position: relative;
    width: 1200px;
    height: 1200px;
  }
  .card {
    position: absolute;
    left: 250px;
    width: 700px;
    height: 400px;
    background: var(--card-navy);
    border-radius: 20px;
    overflow: hidden;
    box-shadow: 0 10px 30px rgba(0, 0, 0, 0.5);
  }
  .card--front { top: 170px; }
  .card--back { top: 630px; }

  .brand-name {
    position: absolute;
    color: var(--accent-lime);
    font-weight: 900;
    line-height: 0.95;
    letter-spacing: 0.5px;
  }
  .card--front .brand-name {
    left: 47px;
    top: 58px;
    font-size: 48px;
  }
  .card--back .brand-name {
    left: 150px;
    top: 110px;
    font-size: 94px;
  }

  .holder {
    position: absolute;
    right: 50px;
    top: 216px;
    text-align: right;
  }
  .holder__name {
    color: var(--text-white);
    font-weight: 900;
    font-size: 33px;
    line-height: 1;
    letter-spacing: 0.3px;
  }
  .holder__role {
    color: var(--accent-lime);
    font-weight: 400;
    font-size: 18.5px;
    margin-top: 6px;
    letter-spacing: 0.3px;
  }
  .divider {
    position: absolute;
    left: 47px;
    top: 286px;
    width: 603px;
    height: 2px;
    background: var(--text-white);
  }
  .contact {
    position: absolute;
    right: 50px;
    top: 304px;
    list-style: none;
    text-align: right;
    color: var(--text-white);
  }
  .contact__item {
    display: flex;
    justify-content: flex-end;
    align-items: center;
    gap: 10px;
  }
  .contact__item--phone { font-size: 20px; height: 26px; }
  .contact__item--email { font-size: 17.5px; height: 26px; margin-top: 0; }
  .contact__icon { width: 13px; height: 13px; flex: none; }
  .card-band {
    position: absolute;
    left: 0;
    bottom: 0;
    width: 700px;
    height: 15px;
  }
</style>
</head>
<body>
<main class="stage">
  <section class="card card--front" aria-label="Card front">
    <div class="brand-name">Halden<br>Nutrition</div>

    <div class="holder">
      <div class="holder__name">MARISA HOLT</div>
      <div class="holder__role">Specialist Rehabilitation Dietitian</div>
    </div>

    <div class="divider"></div>

    <ul class="contact">
      <li class="contact__item contact__item--phone">
        <span>07700900123</span>
        <svg class="contact__icon" viewBox="0 0 24 24" aria-hidden="true">
          <path fill="var(--accent-lime)" d="M6.6 10.8a15.1 15.1 0 0 0 6.6 6.6l2.2-2.2a1 1 0 0 1 1-.25 11.4 11.4 0 0 0 3.6.57 1 1 0 0 1 1 1V20a1 1 0 0 1-1 1A17 17 0 0 1 3 4a1 1 0 0 1 1-1h3.5a1 1 0 0 1 1 1c0 1.25.2 2.45.57 3.57a1 1 0 0 1-.25 1z"/>
        </svg>
      </li>
      <li class="contact__item contact__item--email">
        <span>marisa@haldennutrition.co.uk</span>
        <svg class="contact__icon" viewBox="0 0 24 24" aria-hidden="true">
          <rect x="1" y="4" width="22" height="16" fill="var(--accent-lime)"/>
          <path d="M2 5l10 8 10-8" fill="none" stroke="var(--card-navy)" stroke-width="2"/>
        </svg>
      </li>
    </ul>

    <svg class="card-band" viewBox="0 0 700 15" preserveAspectRatio="none" aria-hidden="true">
      <polygon points="0,0 245,0 232,15 0,15" fill="var(--text-white)"/>
      <polygon points="250,0 700,0 700,15 238,15" fill="var(--accent-lime)"/>
    </svg>
  </section>

  <section class="card card--back" aria-label="Card back">
    <div class="brand-name">Halden<br>Nutrition</div>
  </section>
</main>
</body>
</html>
```